SHOPIFY Store Website- complete design and functionality

I am looking for someone to create a modern and clean looking e-commerce store for our new holiday lighting and decor distribution company through Shopify. We will have a variety of products - greenery (wreaths, garland by size), bows, lighting (different types of lighting - c9 bulbs in various colors, 5mm mini lights, c7) and a variety of accessories needed to install your own lighting and decor.

Need to be complete- ready to use.
thx
Updates

We want a fully functional design including set up on Shopify. Assuming we can give you our Shopify password to get it all set up? Have never done this. Please let us know how it works and what an estimated cost would be or what other details you need to provide pricing estimate. thanks

Target Market(s)

Lighting

Font styles to use
Serif
Sans Serif

Requirements
Must have
• A clean and easy to use interface. We have a shopping cart listed on Shopify already. We would like the website to match our company logo as well.

```html
<!DOCTYPE html>
<html lang="en">
<head>
<meta charset="utf-8">
<title>Brightwell Lights — Holiday Lighting &amp; Decor</title>
<link href="https://fonts.googleapis.com/css2?family=Montserrat:wght@500;600;700&family=Arimo:wght@400&display=swap" rel="stylesheet">
<style>
:root{
  --orange:#f58220;
  --blue:#1662b8;
  --ink:#333333;
  --body:#555555;
  --line:#e4e4e4;
  --dark:#2b2b2b;
  --white:#ffffff;
}
*{box-sizing:border-box;margin:0;padding:0}
html,body{width:1200px;height:4409px;overflow:hidden;background:var(--white)}
body{position:relative;font-family:"Arimo",Arial,sans-serif;color:var(--body)}
.abs{position:absolute}
.head{font-family:"Montserrat",Arial,sans-serif;font-weight:500;color:var(--ink)}
.photo{position:absolute}

.topbar{left:0;top:0;width:1200px;height:51px;background:var(--orange);color:var(--white);
  font:600 12px "Montserrat",sans-serif;text-align:center;line-height:51px}
.nav a{position:absolute;top:105px;font:500 13px "Montserrat",sans-serif;color:var(--ink);text-decoration:none}
.brand{font-family:"Montserrat",sans-serif;font-weight:700;color:var(--blue);letter-spacing:1px}
.brand-head{left:485px;top:88px;width:230px;text-align:center;font-size:34px}

.hero{left:0;top:171px;width:1200px;height:685px;
  background:linear-gradient(180deg,#0f1a3e 0%,#1d2f55 35%,#2a3a2a 60%,#3a3a1a 82%,#4a3a18 100%)}
.hero-title{left:645px;top:355px;font:500 48px "Montserrat",sans-serif;color:var(--white)}
.hero-sub{left:647px;top:425px;width:440px;font:500 23px/36px "Montserrat",sans-serif;color:var(--white)}

.cat-title{position:absolute;width:490px;text-align:center;font:600 26px "Montserrat",sans-serif;color:var(--blue)}
.cat-text{position:absolute;width:400px;text-align:center;font-size:13px;line-height:25px;color:var(--body)}

.section-title{position:absolute;left:0;width:1200px;text-align:center;font:500 28px "Montserrat",sans-serif;color:var(--ink)}
.section-sub{position:absolute;left:0;width:1200px;text-align:center;font-size:13px;color:var(--body)}

.card{position:absolute;top:2089px;width:235px;height:308px;border:1px solid var(--line)}
.card .pic{position:absolute;left:20px;top:18px;width:193px;height:170px}
.card .name{position:absolute;top:220px;width:100%;text-align:center;font:500 17px "Montserrat",sans-serif;color:var(--ink)}
.card .price{position:absolute;top:252px;width:100%;text-align:center;font:600 18px "Montserrat",sans-serif;color:var(--orange)}

.btn{position:absolute;background:var(--orange);color:var(--white);font:500 16px "Montserrat",sans-serif;text-align:center}
.para{position:absolute;font-size:13px;line-height:26px;color:var(--body);text-align:justify}

.news-title{position:absolute;font:500 18px "Montserrat",sans-serif;color:var(--ink)}
.news-date{position:absolute;font:600 13px "Montserrat",sans-serif;color:var(--orange)}

.footer-nav a{position:absolute;top:4253px;font:500 13px "Montserrat",sans-serif;color:var(--ink);text-decoration:none}
.social{position:absolute;top:4243px;width:36px;height:36px;border:1.5px solid #888;border-radius:50%}
.bottombar{left:0;top:4340px;width:1200px;height:69px;background:var(--dark);color:#e0e0e0;
  text-align:center;font-size:13px;line-height:62px}
</style>
</head>
<body>

<div class="abs topbar">WE ARE A HOLIDAY LIGHTING &amp; DECOR STORE</div>

<header class="nav">
  <svg class="abs" style="left:128px;top:105px" width="15" height="15" viewBox="0 0 15 15" aria-label="Search"><circle cx="6" cy="6" r="4.5" fill="none" stroke="#1662b8" stroke-width="2.2"/><line x1="9.5" y1="9.5" x2="14" y2="14" stroke="#1662b8" stroke-width="2.6"/></svg>
  <a style="left:167px">HOME</a>
  <a style="left:258px">ABOUT US</a>
  <a style="left:378px">PRODUCTS</a>
  <div class="abs brand brand-head">BRIGHTWELL</div>
  <a style="left:739px">GALLERY</a>
  <a style="left:844px">SERVICES</a>
  <a style="left:955px">CONTACT US</a>
  <svg class="abs" style="left:1059px;top:105px" width="16" height="14" viewBox="0 0 16 14" aria-label="Cart"><path d="M0 1h3l2 8h8l2-6H4.5" fill="none" stroke="#f58220" stroke-width="2"/><circle cx="6" cy="12" r="1.5" fill="#f58220"/><circle cx="12" cy="12" r="1.5" fill="#f58220"/></svg>
</header>

<section>
  <div class="photo hero" role="img" aria-label="Garden at dusk with string lights, a wicker sofa, candles and a marquee star by a lake"></div>
  <h1 class="abs hero-title">BRIGHTWELL LIGHTS</h1>
  <p class="abs hero-sub">Sed ut perspiciatis unde omnis iste nat us error sit voluptatem</p>
</section>

<section class="categories">
  <div class="photo" style="left:111px;top:945px;width:488px;height:317px;background:linear-gradient(135deg,#1e2a26,#3c4a3e 50%,#8a6a3a)" role="img" aria-label="String lights hanging among pine trees"></div>
  <h2 class="cat-title" style="left:599px;top:1020px">GREENERY</h2>
  <p class="cat-text" style="left:644px;top:1068px">Sed ut perspiciatis unde omnis iste natus error sit voluptatem accusantium doloremque laudantium, totam rem aperiam, eaque ipsa quae ab illo inventore veritatis et quasi architecto beatae vitae dicta sunt explicabo.</p>

  <h2 class="cat-title" style="left:111px;top:1337px">BOWS</h2>
  <p class="cat-text" style="left:156px;top:1385px">Sed ut perspiciatis unde omnis iste natus error sit voluptatem accusantium doloremque laudantium, totam rem aperiam, eaque ipsa quae ab illo inventore veritatis et quasi architecto beatae vitae dicta sunt explicabo.</p>
  <div class="photo" style="left:599px;top:1262px;width:490px;height:317px;background:radial-gradient(circle at 50% 50%,#c8863a,#8a4e1c 60%,#4a2a12)" role="img" aria-label="Tangle of warm white fairy lights"></div>

  <div class="photo" style="left:111px;top:1579px;width:488px;height:318px;background:linear-gradient(135deg,#0b1a4a,#4a1a6a 45%,#1a6a5a 75%,#0a1030)" role="img" aria-label="Colourful holiday light display over water at night"></div>
  <h2 class="cat-title" style="left:599px;top:1655px">LIGHTING</h2>
  <p class="cat-text" style="left:644px;top:1703px">Sed ut perspiciatis unde omnis iste natus error sit voluptatem accusantium doloremque laudantium, totam rem aperiam, eaque ipsa quae ab illo inventore veritatis et quasi architecto beatae vitae dicta sunt explicabo.</p>
</section>

<section class="featured">
  <h2 class="section-title" style="top:1990px">FEATURED PRODUCTS</h2>
  <p class="section-sub" style="top:2038px">Sed ut perspiciatis unde omnis iste natus error sit voluptatem accusantium doloremque</p>

  <div class="card" style="left:111px"><div class="pic" role="img" aria-label="Multicolour mini light string" style="background:radial-gradient(ellipse at center,#4a6a3a,#f6f6f6 70%)"></div><div class="name">PRODUCT NAME</div><div class="price">$25.00</div></div>
  <div class="card" style="left:360px"><div class="pic" role="img" aria-label="Red C9 bulb" style="background:radial-gradient(ellipse 25% 45% at center,#d01818,#fff 100%)"></div><div class="name">PRODUCT NAME</div><div class="price">$25.00</div></div>
  <div class="card" style="left:606px"><div class="pic" role="img" aria-label="Gold and red ornament balls" style="background:radial-gradient(ellipse 45% 30% at center,#b86a3a,#fff 100%)"></div><div class="name">PRODUCT NAME</div><div class="price">$25.00</div></div>
  <div class="card" style="left:853px"><div class="pic" role="img" aria-label="Blue light bulb" style="background:radial-gradient(ellipse 30% 45% at center,#3a7ae0,#fff 100%)"></div><div class="name">PRODUCT NAME</div><div class="price">$25.00</div></div>
</section>

<section class="product">
  <div class="photo" style="left:111px;top:2465px;width:444px;height:514px;border-radius:4px;background:radial-gradient(ellipse at 50% 55%,#b07a3a,#3a2a1a 55%,#120e0a)" role="img" aria-label="Geometric copper pendant lamp glowing"></div>
  <h2 class="abs head" style="left:620px;top:2496px;font-size:27px">SED UT PERSPICIATIS UNDE</h2>
  <div class="abs" style="left:618px;top:2545px;font:500 30px 'Montserrat',sans-serif;color:var(--orange)">$25.00</div>
  <div class="abs" style="left:732px;top:2551px;color:var(--orange);font-size:17px;letter-spacing:2px">★★★★★</div>
  <div class="btn" style="left:620px;top:2607px;width:161px;height:48px;line-height:48px">ADD TO CART</div>
  <p class="para" style="left:620px;top:2684px;width:468px">Sed ut perspiciatis unde omnis iste natus error sit voluptatem accusantium doloremque laudantium, totam rem aperiam, eaque ipsa quae ab illo inventore veritatis et quasi architecto beatae vitae dicta sunt explicabo. Nemo enim ipsam voluptatem quia voluptas sit aspernatur aut odit aut fugit, sed quia consequuntur magni dolores eos qui ratione voluptatem</p>
  <h3 class="abs head" style="left:620px;top:2842px;font-size:18px">PRODUCT DETAILS</h3>
  <p class="para" style="left:620px;top:2880px;width:320px;text-align:left">Sed ut perspiciatis unde omnis iste natus error sit voluptatem accusantium doloremque laudantium, totam rem aperiam,</p>
</section>

<section class="news">
  <h2 class="section-title" style="top:3056px">LATEST NEWS</h2>
  <p class="section-sub" style="top:3103px">Sed ut perspiciatis unde omnis iste natus error sit voluptatem accusantium doloremque</p>

  <div class="photo" style="left:111px;top:3155px;width:476px;height:269px;background:linear-gradient(135deg,#5a0a2a,#1a5a3a 45%,#2a3a8a 75%,#8a1a3a)" role="img" aria-label="Large coloured C9 bulbs outside a house"></div>
  <h3 class="news-title" style="left:111px;top:3445px">SED UT PERSPICIATIS UNDE OMNIS</h3>
  <div class="news-date" style="left:111px;top:3481px">APRIL 02,2021</div>
  <p class="para" style="left:111px;top:3510px;width:478px;text-align:left;font-size:12.5px">Nemo enim ipsam voluptatem quia voluptas sit aspernatur aut odit aut fugit, sed quia consequuntur magni dolores eos qui ratione voluptatem sequi volup tatem quia voluptas sit aspernatur nesciunt.</p>

  <div class="photo" style="left:611px;top:3155px;width:478px;height:269px;background:linear-gradient(135deg,#2a2a2a,#7a7266 50%,#3a3530)" role="img" aria-label="Vintage filament bulbs in geometric frames"></div>
  <h3 class="news-title" style="left:611px;top:3445px">SED UT PERSPICIATIS UNDE OMNIS</h3>
  <div class="news-date" style="left:611px;top:3481px">APRIL 02,2021</div>
  <p class="para" style="left:611px;top:3510px;width:478px;text-align:left;font-size:12.5px">Nemo enim ipsam voluptatem quia voluptas sit aspernatur aut odit aut fugit, sed quia consequuntur magni dolores eos qui ratione voluptatem sequi volup tatem quia voluptas sit aspernatur nesciunt.</p>
</section>

<section class="photo" style="left:0;top:3652px;width:1200px;height:428px;background:radial-gradient(ellipse at 50% 45%,#8a5a1a,#3a2a1a 45%,#1a1e2a 80%)" role="img" aria-label="Glass globe candle holder with bokeh lights">
  <div class="abs brand" style="left:0;top:160px;width:1200px;text-align:center;font-size:110px;color:rgba(255,255,255,0.12)">BRIGHTWELL</div>
</section>

<footer>
  <div class="abs brand" style="left:111px;top:4133px;font-size:40px">BRIGHTWELL</div>
  <div class="abs" style="left:534px;top:4139px;width:373px;height:52px;border:1px solid #cfcfcf;font-size:12px;color:#666;line-height:50px;padding-left:16px">Your Email</div>
  <div class="btn" style="left:919px;top:4139px;width:170px;height:52px;line-height:52px">SUBSCRIBE</div>

  <div class="social" style="left:145px"></div>
  <div class="social" style="left:188px"></div>
  <div class="social" style="left:231px"></div>
  <div class="social" style="left:274px"></div>
  <div class="social" style="left:317px"></div>

  <nav class="footer-nav">
    <a style="left:452px">HOME</a>
    <a style="left:543px">ABOUT US</a>
    <a style="left:664px">PRODUCTS</a>
    <a style="left:787px">GALLERY</a>
    <a style="left:893px">SERVICES</a>
    <a style="left:1004px">CONTACT US</a>
  </nav>

  <div class="abs bottombar">©2021 Brightwell Lights. All rights reserved.</div>
</footer>

</body>
</html>
```